Insurance Broker SaaS Website
Sales Management Software
Project: Insurance Broker SaaS Website
Insurance Broker SaaS Website - Internet Services
Creative Brief
Internet Services
brokerlumen.net
BrokerLumen, LLC is a software development company specializing in lead management software for the commercial P&C and employee benefits insurance markets.
Headquartered in Tampa, Florida, BrokerLumen is uniquely positioned to leverage decades of insurance expertise with state of the art SaaS technology. The solutions was developed by a P&C insurance broker out of frustration for the complexity, cost, and need for IT resources associated with other generic solutions on the market.
Our flagship product, Quota Compass™, provides a simple, user friendly, affordable lead management solution developed specifically for commercial P&C brokers and employee benefits agents. Quota Compass eliminates the need for in-house IT administration and to provide accessibility, scalability, security, data backup, and predictable costs.
BrokerLumen website will focus on two types of users – the P&C broker owner (player/coach) and Employee Benefit Agent/Agencies. We want to emphasize on the home page that it is a P&C/Employee Benefit industry specific software to manage leads and increase sales; it’s simple functionality and it’s low cost; it’s flexible report formats and record layouts (have it your way). A graphic showing sales funnel and where Quota Compass plays may be an idea. Advertising banners (2 OR 3) also will need to be incorporated once we are up and running and have at least one advertiser. It’s important for website to be simple, crisp, clean and compelling. Website should also contain page for industry related articles and a Contact Us/ Comment Section. Also a FAQ about Quota Compass incorporating questions from both types of users. We are offering simplicity and functionality – so website should incorporate this as well. Another idea might be to include some comparisons i.e. Dealwright vs. Quota Compass. Also a “Free 30 day Trial” no credit card required button or buttons should be included at different locations throughout site. Lastly, pricing needs to be prominently displayed throughout: $480.00 annually or $45.00 per month unlimited users. If not completely satisfied within 90 days complete refund.
Service Oriented
Deep Red #990000
Dark Blue
Get creative!
Arial, Verdana, Trebuchet MS
below header
www.taskmoorhq.example
www.vemra.example
www.brisket.example
Website should emphasize increasing sales revenue while offering affordability, functionality and simplicity in a pipeline management system. The goal is to have a CLEAN and SIMPLE layout and website.

```html
<!DOCTYPE html>
<html lang="en">
<head>
<meta charset="utf-8">
<title>BrokerLumen — About My Agency</title>
<link href="https://fonts.googleapis.com/css2?family=Arimo:wght@400;700&display=swap" rel="stylesheet">
<style>
  :root {
    --header: #262c3a;
    --header-line: #3a4254;
    --page: #5c6477;
    --footer: #4b5263;
    --panel: #2c3342;
    --green: #9cc92a;
    --green-light: #c4e45a;
    --green-dark: #6f9a12;
    --ink-dark: #24300a;
    --text: #dde1ea;
    --muted: #b9bfcc;
    --white: #ffffff;
    --accent: #c8ee4c;
  }
  * { box-sizing: border-box; margin: 0; padding: 0; }
  html, body { width: 1200px; height: 931px; overflow: hidden; }
  body { background: var(--page); font-family: "Arimo", Arial, sans-serif; color: var(--text); position: relative; }
  a { text-decoration: none; }

  .site-header { position: absolute; left: 0; top: 0; width: 1200px; height: 80px; background: linear-gradient(#303746, var(--header)); border-bottom: 1px solid var(--header-line); }
  .brand { position: absolute; left: 352px; top: 24px; }
  .brand-name { font-size: 22px; font-weight: 700; color: var(--white); letter-spacing: .5px; }
  .brand-tag { font-size: 8px; color: var(--muted); margin-top: 2px; letter-spacing: .5px; }
  .utility { position: absolute; left: 672px; top: 6px; font-size: 8px; color: var(--muted); }
  .utility span { margin-right: 10px; }
  .main-nav { position: absolute; left: 530px; top: 31px; display: flex; align-items: center; gap: 24px; font-size: 11px; color: var(--white); }
  .main-nav .active { background: linear-gradient(var(--green-light), var(--green)); color: var(--ink-dark); border-radius: 12px; padding: 5px 14px; font-weight: 700; }

  .profile-note { position: absolute; left: 918px; top: 28px; width: 124px; height: 140px; transform: rotate(4deg); }
  .profile-note .sheet { position: absolute; inset: 0; background: linear-gradient(135deg, var(--green-light), var(--green) 60%, var(--green-dark)); box-shadow: 2px 4px 8px rgba(0,0,0,.35); }
  .profile-note .tape { position: absolute; left: 32px; top: -10px; width: 60px; height: 18px; background: rgba(230,240,200,.55); }
  .profile-note h4 { position: absolute; left: 10px; top: 14px; font-size: 9px; color: var(--white); }
  .profile-note p { position: absolute; left: 10px; top: 30px; right: 10px; font-size: 6.5px; line-height: 9px; color: var(--ink-dark); }
  .profile-note .go { position: absolute; left: 10px; bottom: 14px; width: 62px; height: 13px; border-radius: 7px; background: var(--green-dark); color: var(--white); font-size: 6.5px; font-weight: 700; display: flex; align-items: center; justify-content: center; }

  .content { position: absolute; left: 352px; top: 100px; width: 486px; }
  h1, h2 { font-size: 12px; color: var(--white); font-weight: 700; }
  .copy { font-size: 8px; line-height: 11px; color: var(--text); }
  .copy em { font-style: normal; font-weight: 700; color: var(--accent); }
  .intro { position: absolute; left: 0; top: 22px; width: 486px; }
  .with-photo { position: absolute; left: 0; top: 58px; width: 356px; }
  .photo { position: absolute; left: 373px; top: 58px; width: 113px; height: 118px; border: 3px solid #e9ecf1; background: linear-gradient(135deg, #e8ecf2, #9aa3b3 55%, #3c4353); }
  .wide { position: absolute; left: 0; top: 192px; width: 486px; }
  .services-title { position: absolute; left: 0; top: 247px; }
  .services { position: absolute; left: 0; top: 268px; list-style: none; width: 340px; }
  .services li { font-size: 8px; height: 19px; padding-left: 12px; position: relative; color: var(--text); }
  .services li::before { content: ""; position: absolute; left: 0; top: 2px; width: 5px; height: 5px; border-radius: 50%; background: var(--green); }

  .side-panel { position: absolute; left: 704px; top: 327px; width: 134px; height: 159px; background: var(--panel); border-radius: 6px; box-shadow: 0 2px 6px rgba(0,0,0,.3); }
  .side-panel .badge { position: absolute; left: -8px; top: 8px; width: 20px; height: 20px; border-radius: 50%; background: var(--green); border: 2px solid #e6f3b8; }
  .side-panel .pill { position: absolute; right: 8px; top: 4px; width: 22px; height: 8px; border-radius: 4px; background: var(--green); }
  .side-panel h3 { position: absolute; left: 24px; top: 12px; font-size: 10px; color: var(--white); }
  .side-panel ul { position: absolute; left: 12px; top: 36px; right: 8px; list-style: none; }
  .side-panel li { font-size: 7px; height: 19px; color: var(--muted); padding-left: 9px; position: relative; border-bottom: 1px solid #3a4252; padding-top: 5px; }
  .side-panel li::before { content: ""; position: absolute; left: 0; top: 8px; width: 4px; height: 4px; background: var(--green); }

  .cta { position: absolute; left: 704px; width: 134px; height: 30px; border-radius: 15px; background: linear-gradient(var(--green-light), var(--green) 55%, var(--green-dark)); color: var(--white); font-size: 11px; font-weight: 700; display: flex; align-items: center; padding-left: 22px; box-shadow: 0 2px 4px rgba(0,0,0,.3); }

  .pager { position: absolute; left: 604px; top: 692px; width: 232px; height: 20px; background: var(--panel); border-radius: 10px; font-size: 8px; color: var(--muted); display: flex; align-items: center; justify-content: space-between; padding: 0 20px; }
  .pager b { color: var(--white); }

  .site-footer { position: absolute; left: 0; top: 725px; width: 1200px; height: 206px; background: var(--footer); border-top: 1px solid #6a7285; }
  .fcol { position: absolute; top: 12px; }
  .fcol h5 { font-size: 8px; color: var(--white); margin-bottom: 8px; }
  .fcol ul { list-style: none; }
  .fcol li { font-size: 7px; line-height: 12px; color: var(--muted); }
  .fcol p { font-size: 6.5px; line-height: 9px; color: var(--muted); margin-bottom: 6px; }
  .social { position: absolute; left: 516px; top: 110px; display: flex; gap: 6px; }
  .social span { width: 14px; height: 14px; background: #8fa0c4; border-radius: 2px; }
  .social span:nth-child(2) { background: #7cb7e0; }
  .social span:nth-child(3) { background: #c8d1e0; }
  .social span:nth-child(4) { background: #6b87b8; }
  .trial-button { position: absolute; left: 680px; top: 110px; width: 62px; height: 14px; border-radius: 7px; background: linear-gradient(var(--green-light), var(--green)); color: var(--ink-dark); font-size: 6.5px; font-weight: 700; display: flex; align-items: center; justify-content: center; }
  .credit { position: absolute; left: 800px; top: 180px; width: 60px; font-size: 7px; color: var(--muted); text-align: right; line-height: 10px; }
  .copyright { position: absolute; left: 0; width: 1200px; top: 194px; text-align: center; font-size: 6.5px; color: var(--muted); }
</style>
</head>
<body>

<header class="site-header">
  <div class="brand">
    <div class="brand-name">BrokerLumen</div>
    <div class="brand-tag">my trusted company</div>
  </div>
  <div class="utility"><span>Client Login</span><span>Sign Up</span><span>FAQ</span></div>
  <nav class="main-nav">
    <span>Home</span>
    <span class="active">About Us</span>
    <span>Contact US</span>
    <span>Blog</span>
    <span>Products</span>
  </nav>
</header>

<aside class="profile-note">
  <div class="sheet"></div>
  <div class="tape"></div>
  <h4>My Profile</h4>
  <p>Quota Compass: $45 a month or $480 a year, unlimited users. Full refund within 90 days.</p>
  <a class="go">Free 30 Day Trial</a>
</aside>

<main class="content">
  <h1>About My Agency</h1>
  <p class="copy intro">BrokerLumen builds lead management software for commercial P&amp;C brokers and employee benefits agents. <em>Quota Compass is $480 a year or $45 a month, unlimited users</em>, with a free 30 day trial and no credit card required to get started today.</p>
  <p class="copy with-photo">Headquartered in Tampa, Florida, BrokerLumen pairs decades of insurance experience with modern SaaS technology. Quota Compass was created by a P&amp;C broker tired of the cost and complexity of generic sales tools. It needs no in-house IT, and gives you secure access anywhere, automatic data backup, flexible report formats and record layouts, and a predictable monthly cost. Track every lead from first call to bound policy and see exactly where each prospect sits in your sales funnel.</p>
  <div class="photo" role="img" aria-label="Photo of an insurance agent at a desk with a laptop"></div>
  <p class="copy wide">Simple to learn and simple to use, Quota Compass helps the broker owner coach a team and helps benefits agents grow revenue. Not completely satisfied within 90 days? You get a complete refund.</p>

  <h2 class="services-title">Insurance Services</h2>
  <ul class="services">
    <li>Commercial property coverage for growing firms</li>
    <li>General liability plans with flexible limits</li>
    <li>Employee benefits packages for small teams</li>
    <li>Workers compensation quotes in one day</li>
    <li>Group health plans tailored to your staff</li>
    <li>Business auto and fleet protection options</li>
    <li>Professional liability for service companies</li>
    <li>Umbrella policies for added peace of mind</li>
    <li>Cyber risk coverage for client data and systems</li>
    <li>Dental and vision plans for every employee</li>
    <li>Life and disability income protection plans</li>
    <li>Inland marine and equipment coverage</li>
    <li>Builders risk policies for new projects</li>
    <li>Key person coverage for business owners</li>
    <li>Renewal reviews with clear side by side quotes</li>
    <li>Claims support from a dedicated local broker</li>
    <li>Annual risk reviews and policy check ups</li>
  </ul>
</main>

<section class="side-panel">
  <div class="badge"></div>
  <div class="pill"></div>
  <h3>Your Insurance</h3>
  <ul>
    <li>Review your current coverage</li>
    <li>Compare carrier quotes</li>
    <li>Quota Compass FAQ</li>
    <li>Dealwright vs. Quota Compass</li>
    <li>Report a new claim online</li>
    <li>Download your documents</li>
  </ul>
</section>

<a class="cta" style="top:516px">What's Insurance</a>
<a class="cta" style="top:566px">Benefits</a>
<a class="cta" style="top:615px">Important Tips</a>

<nav class="pager"><b>&lt; Previous</b><span>1 2 3 4 5 6 ... 205</span><b>Next &gt;</b></nav>

<footer class="site-footer">
  <div class="fcol" style="left:352px">
    <h5>Partners</h5>
    <ul><li>Home</li><li>About</li><li>Contact Us</li><li>Blog</li><li>FAQ</li></ul>
  </div>
  <div class="fcol" style="left:516px; width:150px">
    <h5>About Design Lab</h5>
    <p>BrokerLumen helps commercial brokers and benefits agents manage leads, follow up faster and close more business with less effort.</p>
    <p>Our tools are simple to learn, priced fairly and built by people who have sold insurance for years.</p>
    <p>Start a free thirty day trial today, no credit card is needed to begin.</p>
  </div>
  <div class="fcol" style="left:676px; width:150px">
    <h5>Recommend</h5>
    <p>Quota Compass keeps every prospect, quote and renewal in one clear pipeline so nothing slips through the cracks.</p>
    <p>Just $45 a month or $480 a year, with unlimited users and flexible reports included.</p>
    <p>Not satisfied within ninety days? You get a complete refund.</p>
  </div>
  <div class="social"><span></span><span></span><span></span><span></span></div>
  <a class="trial-button">Free Trial</a>
  <div class="credit">Design by<br>Studio Team</div>
  <div class="copyright">© BrokerLumen, LLC. All rights reserved.</div>
</footer>

</body>
</html>
```